Box design for superfood powders

Hey,
I am creating a new brand of superfoods mixes in and I am looking for a designer to create the design for the box.
I have for 4 products on the roadmap, but I need the design just for the first one:
- For skin nails and hair benefits: Collagen + CoQ10 and Vitamin C powders (eg: Blueberries, Camu Camu, Acai)
- For energy and immune system (eg: mushrooms powder)
- Green Mix (eg: Spirulina + Wheatgrass + Chlorella)
- Protein mix (eg: hemp + rice powders)
I will use Kraft paper for the box so I am able to print max 2 colors on them (black and another color distinctive for each specific powder mix).
I need the design just for the first one with collagen, because all the products will have the same format. I will just change the name, ingredients and the color
More details in the archive attached.

Updates
Low design quality
Target Market(s)
woman between 30-50
Requirements
Should not have
- Ilustrations with fruits or flowers
Just shapes and colors

```html
<!DOCTYPE html>
<html lang="en">
<head>
<meta charset="utf-8">
<title>Velvet Collagen – box dieline</title>
<link rel="stylesheet" href="https://fonts.googleapis.com/css2?family=Poppins:wght@400;500;600;700&display=swap">
<style>
  :root {
    --kraft: #d9a77c;
    --ink: #111111;
    --cut: #1a1a2e;
    --fold: #e8312f;
  }
  html, body {
    margin: 0;
    padding: 0;
    width: 1200px;
    height: 1080px;
    overflow: hidden;
    background: var(--kraft);
  }
  .dieline {
    display: block;
    width: 1200px;
    height: 1080px;
    font-family: "Poppins", sans-serif;
  }
  .cut-line { fill: none; stroke: var(--cut); stroke-width: 1.2; }
  .fold-line { fill: none; stroke: var(--fold); stroke-width: 1.2; }
  .ink { fill: var(--ink); }
  .brand-dot { fill: var(--ink); }
  .brand-name { fill: var(--ink); font-weight: 600; }
  .product-title { fill: var(--ink); font-weight: 400; text-anchor: middle; }
  .tagline { fill: var(--ink); font-weight: 600; text-anchor: middle; }
  .body-copy { fill: var(--ink); font-size: 7.6px; }
  .table-title { font-size: 7px; }
  .tiny { font-size: 4.5px; }
  .badge-label { font-size: 5.5px; }
  .label-bold { font-weight: 600; }
  .rule { stroke: #5a4330; stroke-width: 0.8; }
  .icon-stroke { fill: none; stroke: var(--ink); stroke-width: 2; }
  .table-line { stroke: #3a2a1e; stroke-width: 0.7; fill: none; }
</style>
</head>
<body>
<svg class="dieline" viewBox="0 35 1280 1093" preserveAspectRatio="xMidYMid meet" xmlns="http://www.w3.org/2000/svg">
  <rect x="0" y="0" width="1280" height="1164" fill="var(--kraft)"/>

  <g class="cut-lines">
    <rect class="cut-line" x="80" y="365" width="1077" height="422"/>
    <path class="cut-line" d="M80,365 L93,233 L323,233 L337,330 L349,336 L349,365"/>
    <path class="cut-line" d="M619,365 L619,336 L631,330 L645,233 L877,233 L885,365"/>
    <path class="cut-line" d="M887,365 L887,95 L890,95 L890,75 Q890,52 913,52 L1133,52 Q1156,52 1156,75 L1156,95 L1157,95 L1157,365"/>
    <path class="cut-line" d="M1157,365 L1200,370 L1200,783 L1157,787"/>
    <path class="cut-line" d="M80,787 L80,810 L93,820 L108,918 L333,918 L340,822 L349,790"/>
    <path class="cut-line" d="M621,787 L627,820 L634,918 L864,918 L877,878 L886,822 L887,787"/>
    <path class="cut-line" d="M349,787 L349,1055 L351,1055 L351,1078 Q351,1100 373,1100 L595,1100 Q617,1100 617,1078 L617,1055 L619,1055 L619,787"/>
    <line class="cut-line" x1="349" y1="365" x2="349" y2="787"/>
    <line class="cut-line" x1="887" y1="365" x2="887" y2="787"/>
  </g>

  <g class="fold-lines">
    <line class="fold-line" x1="619" y1="365" x2="1157" y2="365"/>
    <line class="fold-line" x1="80" y1="787" x2="887" y2="787"/>
    <line class="fold-line" x1="619" y1="365" x2="619" y2="787"/>
    <line class="fold-line" x1="1157" y1="365" x2="1157" y2="787"/>
    <line class="fold-line" x1="917" y1="97" x2="1128" y2="97"/>
    <line class="fold-line" x1="378" y1="1055" x2="589" y2="1055"/>
  </g>

  <!-- Lid (upside down) -->
  <g class="lid-panel" transform="rotate(180 1022 210)">
    <text class="tagline" x="1022" y="246" font-size="12">Rise into your best days</text>
    <circle class="brand-dot" cx="984" cy="187" r="9"/>
    <text class="brand-name" x="999" y="195" font-size="22">lumera</text>
  </g>

  <!-- Left side panel -->
  <g class="side-panel">
    <circle class="brand-dot" cx="188" cy="404" r="7"/>
    <text class="brand-name" x="200" y="410" font-size="17">lumera</text>
    <text class="product-title" x="217" y="468" font-size="24">Velvet</text>
    <text class="product-title" x="217" y="497" font-size="24">Collagen</text>
    <text class="body-copy" x="107" y="527">
      <tspan x="107">We make it easy for busy people to look and feel good</tspan>
      <tspan x="107" dy="12">about their appearance. Just add Velvet Collagen</tspan>
      <tspan x="107" dy="12">powder to your favorite smoothie or milk and get the</tspan>
      <tspan x="107" dy="12">extra dose of collagen and skin protecting antioxidants.</tspan>
      <tspan x="107" dy="12">It helps combat the effects of free radicals and may</tspan>
      <tspan x="107" dy="12">restore your natural plumpness.</tspan>
    </text>
    <line class="rule" x1="107" y1="603" x2="326" y2="603"/>
    <circle class="icon-stroke" cx="123" cy="629" r="14"/>
    <path class="ink" d="M116,637 Q116,620 131,619 Q131,635 116,637 Z"/>
    <text class="body-copy badge-label label-bold" x="123" y="652" text-anchor="middle">NATURAL</text>
    <text class="body-copy" x="180" y="618">
      <tspan x="180" class="label-bold">Ingredients:</tspan>
      <tspan x="180" dy="10">• Type 1 Marine Collagen</tspan>
      <tspan x="180" dy="10">• CoQ10</tspan>
      <tspan x="180" dy="10">• Hyaluronic acid powder</tspan>
      <tspan x="180" dy="10">• Camu Camu</tspan>
      <tspan x="180" dy="10">• Rosehip</tspan>
      <tspan x="180" dy="10">• Sea buckthorn</tspan>
      <tspan x="180" dy="10">• Banana</tspan>
      <tspan x="180" dy="10">• Date</tspan>
      <tspan x="180" dy="10">• Acai</tspan>
    </text>
    <circle class="icon-stroke" cx="122" cy="740" r="14"/>
    <line class="icon-stroke" x1="112" y1="730" x2="132" y2="750"/>
    <circle class="icon-stroke" cx="158" cy="740" r="14"/>
    <line class="icon-stroke" x1="148" y1="730" x2="168" y2="750"/>
    <text class="body-copy" x="180" y="731">
      <tspan x="180"><tspan class="label-bold">Free from:</tspan> Gluten, Dairy, Soy, GMO,</tspan>
      <tspan x="180" dy="10">sweeteners, fillers, additives,</tspan>
      <tspan x="180" dy="10">preservatives or anything artificial.</tspan>
    </text>
  </g>

  <!-- Front panel -->
  <g class="front-panel">
    <circle class="brand-dot" cx="440" cy="459" r="10"/>
    <text class="brand-name" x="456" y="468" font-size="25">lumera</text>
    <text class="tagline" x="484" y="516" font-size="11.5">Rise into your best days</text>
    <text class="product-title" x="484" y="594" font-size="33">Velvet</text>
    <text class="product-title" x="484" y="633" font-size="33">Collagen</text>
    <line class="rule" x1="380" y1="701" x2="590" y2="701"/>
    <text class="product-title" x="484" y="719" font-size="11">Get the extra dose of collagen and</text>
    <text class="product-title" x="484" y="733" font-size="11">skin protecting antioxidants</text>
    <line class="rule" x1="380" y1="745" x2="590" y2="745"/>
    <text class="body-copy label-bold" x="601" y="772" text-anchor="end">14 portions x 10g = 140g</text>
  </g>

  <!-- Back panel -->
  <g class="back-panel">
    <g class="nutrition-table">
      <rect class="table-line" x="681" y="422" width="99" height="95"/>
      <text class="body-copy table-title label-bold" x="731" y="432" text-anchor="middle">Nutrition Value table</text>
      <text class="body-copy tiny label-bold" x="731" y="439" text-anchor="middle">Per sachet</text>
      <line class="table-line" x1="681" y1="445" x2="780" y2="445"/>
      <line class="table-line" x1="681" y1="457" x2="780" y2="457"/>
      <line class="table-line" x1="681" y1="469" x2="780" y2="469"/>
      <line class="table-line" x1="681" y1="481" x2="780" y2="481"/>
      <line class="table-line" x1="681" y1="493" x2="780" y2="493"/>
      <line class="table-line" x1="681" y1="505" x2="780" y2="505"/>
      <line class="table-line" x1="733" y1="445" x2="733" y2="517"/>
    </g>
    <g class="icon-cup">
      <path class="icon-stroke" stroke-width="1.2" d="M640,526 L650,523 L652,530 L642,533 Z M650,530 L660,541"/>
      <path class="icon-stroke" stroke-width="1.4" d="M651,543 L671,543 L669,554 L653,554 Z M671,545 Q676,548 670,551 M647,558 L675,558"/>
    </g>
    <text class="body-copy" x="682" y="535">
      <tspan x="682" class="label-bold">How to use it:</tspan>
      <tspan x="682" dy="12">Add one pack to your water, smoothies,</tspan>
      <tspan x="682" dy="12">yoghurt, musli, oatmeal.</tspan>
    </text>
    <circle class="icon-stroke" cx="657" cy="591" r="14" stroke-width="1.6"/>
    <text class="body-copy tiny" x="657" y="587" text-anchor="middle">15°-30°C</text>
    <rect class="ink" x="651" y="590" width="12" height="10"/>
    <text class="body-copy" x="682" y="595"><tspan class="label-bold">Storage:</tspan> Keep closed in a cool dry place</text>
    <text class="body-copy" x="642" y="643"><tspan class="label-bold">Produced by.</tspan> Norvik SRL for Brightway SRL</text>
    <text class="body-copy" x="642" y="657">
      <tspan x="642" class="label-bold">Connect:</tspan>
      <tspan x="642" dy="10">Call +40 700 123 456</tspan>
      <tspan x="642" dy="10">visit our website <tspan class="label-bold">www.lumera.com/ro/start</tspan></tspan>
    </text>
    <circle class="ink" cx="832" cy="765" r="11"/>
    <path d="M826,767 A6,6 0 1 1 836,770 M836,770 L838,764 M836,770 L831,768" fill="none" stroke="var(--kraft)" stroke-width="1.8"/>
    <circle class="ink" cx="870" cy="756" r="2.5"/>
    <path class="icon-stroke" stroke-width="1.6" d="M870,760 L870,774 M870,774 L867,774 M870,766 L873,771 M858,763 L866,763 L864,774 L860,774 Z"/>
  </g>
</svg>
</body>
</html>
```